Simple but elegant business card/logo design for exclusive beauty business

We need a logo designed for a new elegant and exclusive beauty business called "R". The logo itself should be a stylistic and custom design for the letter "R". We would like the business card to have the logo as the centrepiece on a clean background. Gold Logo on black background or silver on white background.

The business card details should be displayed centre of the card. Details are as follows:

Tamsin Earle
Facebook: /shinesoftlyr
Instagram: /shinesoftlyr

The words "Shine Softly" should also appear somewhere on the card.

Industry/Entity Type

Business

Logo Text

G

Requirements
Must have
• Design must be simple, clean and elegant
Should not have
• The design should not be cluttered

```html
<!DOCTYPE html>
<html lang="en">
<head>
<meta charset="utf-8">
<title>Tamsin Earle – Business Card</title>
<link href="https://fonts.googleapis.com/css2?family=Roboto:wght@400;500;700&display=swap" rel="stylesheet">
<style>
  :root {
    --backdrop: #e8e9eb;
    --gold: #c4ab3b;
    --charcoal: #2f2d2e;
    --ink: #1e1d1d;
    --card-w: 520px;
    --card-h: 300px;
  }
  * { box-sizing: border-box; margin: 0; padding: 0; }
  html, body {
    width: 1200px;
    height: 800px;
    overflow: hidden;
    background: var(--backdrop);
    font-family: "Roboto", Arial, sans-serif;
  }
  .card-sheet {
    width: 1200px;
    height: 800px;
    display: flex;
    align-items: center;
    justify-content: center;
    gap: 60px;
  }
  .card {
    position: relative;
    width: var(--card-w);
    height: var(--card-h);
    box-shadow: 0 14px 30px rgba(0,0,0,0.22);
    overflow: hidden;
  }

  /* Front */
  .card--front { background: var(--gold); }
  .card__band {
    position: absolute;
    top: 0;
    left: 34px;
    width: 200px;
    height: 100%;
    background: var(--charcoal);
    display: flex;
    align-items: center;
    justify-content: center;
  }
  .card__details {
    position: absolute;
    top: 0;
    left: 234px;
    right: 0;
    height: 100%;
    padding: 0 34px 0 30px;
    display: flex;
    flex-direction: column;
    justify-content: center;
    color: var(--ink);
  }
  .tagline {
    align-self: center;
    border: 1.5px solid var(--ink);
    padding: 4px 14px;
    font-size: 12px;
    font-weight: 400;
    letter-spacing: 0.3px;
    margin-bottom: 14px;
  }
  .owner-name {
    text-align: center;
    font-size: 27px;
    font-weight: 700;
    text-transform: uppercase;
    letter-spacing: 0.5px;
    line-height: 1;
  }
  .divider {
    height: 2px;
    background: var(--ink);
    margin: 14px 0 16px;
  }
  .contact-list {
    list-style: none;
    font-size: 10.5px;
    line-height: 1.55;
  }
  .contact-list .business-line { font-weight: 500; margin-bottom: 2px; }
  .contact-list .address { display: flex; align-items: center; gap: 4px; margin-bottom: 6px; }
  .contact-list .address svg { width: 8px; height: 11px; flex: none; }

  /* Monogram */
  .monogram {
    display: flex;
    align-items: center;
    justify-content: center;
    border-radius: 50%;
    border: 3px solid var(--gold);
    color: var(--gold);
    font-weight: 700;
    line-height: 1;
  }
  .monogram--small { width: 104px; height: 104px; font-size: 56px; }
  .monogram--large { width: 136px; height: 136px; font-size: 74px; border-width: 4px; }

  /* Back */
  .card--back {
    background: var(--charcoal);
    display: flex;
    align-items: center;
    justify-content: center;
  }
  .card__frame {
    position: absolute;
    inset: 22px;
    border: 2px solid var(--gold);
  }
</style>
</head>
<body>
  <main class="card-sheet">
    <section class="card card--front" aria-label="Business card front">
      <div class="card__band">
        <div class="monogram monogram--small" aria-label="R">R</div>
      </div>
      <div class="card__details">
        <p class="tagline">Shine Softly</p>
        <h1 class="owner-name">Tamsin Earle</h1>
        <div class="divider"></div>
        <ul class="contact-list">
          <li class="business-line">elegant and exclusive beautybusiness</li>
          <li class="address">
            <svg viewBox="0 0 8 11" aria-hidden="true"><path d="M4 0C1.8 0 0 1.7 0 3.9 0 6.8 4 11 4 11s4-4.2 4-7.1C8 1.7 6.2 0 4 0zm0 5.4a1.5 1.5 0 1 1 0-3 1.5 1.5 0 0 1 0 3z" fill="currentColor"/></svg>
            418 Willow Lane Portland OR 97201
          </li>
          <li>Facebook: /shinesoftlyr</li>
          <li>Instagram: /shinesoftlyr</li>
        </ul>
      </div>
    </section>

    <section class="card card--back" aria-label="Business card back">
      <div class="card__frame"></div>
      <div class="monogram monogram--large" aria-label="R">R</div>
    </section>
  </main>
</body>
</html>
```